Shoes & Inserts Postcard Campaign

Hi,
We are looking to send a postcard to our patients reminding them that they may be eligible for shoes and inserts in the new calendar year. The patient demographic is mostly 50 and above.

We plan on uploading the image to Brimo Cards and have them create the postcard for us to be sent out.
Dimensions: 4.2"x5.5"
Front & Back Design
Images should be in high resolution. Entire postcard to be high resolution, if not vector.
I've attached a sample of what we used to have with the dimension parameters and our logo.

Verbiage can be the same, switch it to 2023. Front of the postcard doesn't need our logo. Looking for eye catching. Warm and welcoming.

Thank you,
Darren Osk

```html
<!DOCTYPE html>
<html lang="en">
<head>
<meta charset="utf-8">
<title>Linden Foot &amp; Ankle — Shoes &amp; Inserts Postcard</title>
<link href="https://fonts.googleapis.com/css2?family=Fira+Sans+Condensed:wght@500;600;700&family=Fira+Sans:wght@500;600&family=Noto+Serif:wght@400&display=swap" rel="stylesheet">
<style>
  :root{
    --stage:#8f8f8f;
    --white:#ffffff;
    --orange:#f0845a;
    --peach:#f9c4a8;
    --teal:#4cc0a0;
    --mint:#1ef5c3;
    --ink:#141414;
    --mail:#e0e0e0;
    --alert:#ff1a1a;
    --text:#1b1b1b;
  }
  *{margin:0;padding:0;box-sizing:border-box}
  html,body{width:1049px;height:1200px;overflow:hidden;background:var(--stage)}
  body{position:relative;font-family:"Fira Sans",sans-serif}
  .card{position:absolute;left:236px;width:577px;height:441px;background:var(--white);overflow:hidden;box-shadow:0 1px 4px rgba(0,0,0,.35)}
  .card--front{top:131px}
  .card--back{top:628px}
  .card svg.shapes{position:absolute;inset:0;width:577px;height:441px}
  .abs{position:absolute}
  .brand{display:flex;align-items:center;gap:8px;color:var(--orange);font-family:"Fira Sans Condensed",sans-serif;font-weight:700;line-height:.95;text-transform:uppercase}
  .brand__dot{width:24px;height:24px;border-radius:50%;background:var(--teal);flex:none}
  .brand__name{font-size:17px;text-align:right}
  .brand__name small{display:block;font-size:7.5px;margin-top:2px}
  .headline{right:47px;top:166px;color:var(--white);font-family:"Fira Sans Condensed",sans-serif;font-weight:700;text-align:right;line-height:1;text-transform:uppercase;text-shadow:0 1px 3px rgba(0,0,0,.25)}
  .headline__big{font-size:64px;line-height:58px}
  .headline__mid{font-size:31px;line-height:30px;font-weight:600;margin-top:2px}
  .headline__low{font-size:37px;line-height:32px;font-weight:600}
  .contact{left:22px;top:364px;font-family:"Fira Sans Condensed",sans-serif;text-transform:uppercase;line-height:1}
  .contact__lead{color:var(--teal);font-size:20px;font-weight:500}
  .contact__phone{color:var(--orange);font-size:31px;font-weight:700;margin-top:0}
  .contact__web{color:var(--teal);font-size:18px;font-weight:600;margin-top:1px;letter-spacing:.2px}
  .address{left:31px;top:68px;font-family:"Noto Serif",serif;font-size:12px;color:var(--text);line-height:14.5px;font-style:normal}
  .tagline{left:217px;top:26px;color:var(--orange);font-family:"Fira Sans Condensed",sans-serif;font-weight:700;text-transform:uppercase;line-height:.95}
  .tagline__big{font-size:52px;letter-spacing:.5px}
  .tagline__small{font-size:39px}
  .notice{left:0;width:293px;top:152px;text-align:center;color:var(--white)}
  .notice__lead{font-size:16.5px;line-height:19px;font-weight:500}
  .notice__lead em{font-style:normal;color:var(--alert)}
  .notice__call{color:var(--teal);font-size:14.5px;line-height:15px;font-weight:500;margin-top:8px}
  .notice__away{color:var(--orange);font-family:"Noto Serif",serif;font-size:14.5px;margin-top:10px}
  .notice__phone{font-size:33px;font-weight:600;line-height:1;margin-top:2px}
  .notice__fine{font-family:"Fira Sans Condensed",sans-serif;font-size:9px;line-height:12px;font-weight:600;margin-top:10px}
</style>
</head>
<body>

<section class="card card--front">
  <svg class="shapes" viewBox="0 0 577 441">
    <defs>
      <radialGradient id="trail" cx="0.42" cy="0.12" r="0.95" fx="0.42" fy="0.08">
        <stop offset="0" stop-color="#fbe7a6"/>
        <stop offset=".18" stop-color="#efc27a"/>
        <stop offset=".45" stop-color="#c98a55"/>
        <stop offset=".75" stop-color="#a56a40"/>
        <stop offset="1" stop-color="#6f4128"/>
      </radialGradient>
      <radialGradient id="insoleA" cx=".45" cy=".4" r=".7">
        <stop offset="0" stop-color="#eeeeea"/>
        <stop offset=".55" stop-color="#b9bdb6"/>
        <stop offset="1" stop-color="#6f7a70"/>
      </radialGradient>
      <linearGradient id="insoleB" x1="0" y1="0" x2="0" y2="1">
        <stop offset="0" stop-color="#b98a84"/>
        <stop offset=".45" stop-color="#e2cfc2"/>
        <stop offset="1" stop-color="#ffffff"/>
      </linearGradient>
    </defs>
    <rect width="577" height="441" fill="url(#trail)" role="img" aria-label="Photo: walker in running shoes on a sunlit forest trail"/>
    <path d="M270,0 C340,75 410,150 577,154 L577,0 Z" fill="var(--white)"/>
    <path d="M272,0 C342,75 410,150 577,152" fill="none" stroke="var(--peach)" stroke-width="7"/>
    <path d="M270,0 C345,82 412,158 577,162" fill="none" stroke="var(--orange)" stroke-width="4"/>
    <path d="M0,292 C60,335 150,365 260,366 C380,367 470,372 577,405 L577,441 L0,441 Z" fill="var(--white)"/>
    <path d="M0,284 C60,327 150,358 260,359 C380,360 470,366 577,398" fill="none" stroke="var(--teal)" stroke-width="9"/>
    <path d="M0,294 C60,336 150,367 260,367 C380,368 470,375 577,408" fill="none" stroke="var(--mint)" stroke-width="8"/>
    <circle cx="316" cy="355" r="68" fill="var(--peach)" opacity=".55"/>
    <circle cx="316" cy="355" r="62" fill="url(#insoleA)" role="img" aria-label="Photo: hands holding a yellow shoe insert and a black sneaker"/>
    <circle cx="471" cy="367" r="63" fill="var(--peach)" opacity=".55"/>
    <circle cx="471" cy="367" r="57" fill="url(#insoleB)" role="img" aria-label="Photo: custom orthotic insert held under a foot"/>
  </svg>

  <div class="abs brand" style="right:25px;top:34px">
    <span class="brand__dot"></span>
    <span class="brand__name">Linden<br>Foot &amp; Ankle<small>steadystride.com</small></span>
  </div>

  <h1 class="abs headline">
    <div class="headline__big">Have You</div>
    <div class="headline__mid">Ordered this year's</div>
    <div class="headline__low">Shoes &amp; Inserts?</div>
  </h1>

  <div class="abs contact">
    <div class="contact__lead">Call us today</div>
    <div class="contact__phone">877-555-0142</div>
    <div class="contact__web">www.steadystride.com</div>
  </div>
</section>

<section class="card card--back">
  <svg class="shapes" viewBox="0 0 577 441">
    <rect width="577" height="441" fill="var(--mail)"/>
    <rect width="450" height="137" fill="var(--white)"/>
    <path d="M0,112 L0,441 L70,441 L70,367 L293,367 L293,134 C230,128 160,126 100,132 C55,136 25,128 0,112 Z" fill="var(--ink)"/>
    <path d="M0,102 C40,124 90,126 160,120 C240,112 300,114 360,136" fill="none" stroke="var(--peach)" stroke-width="7"/>
    <path d="M0,108 C40,130 90,132 160,126 C230,120 280,122 320,137" fill="none" stroke="var(--orange)" stroke-width="4"/>
    <path d="M0,338 L0,441 L70,441 Z" fill="var(--white)"/>
    <path d="M0,346 L66,441" stroke="var(--mint)" stroke-width="7"/>
    <path d="M0,332 L70,428" stroke="var(--teal)" stroke-width="4"/>
  </svg>

  <div class="abs brand" style="left:31px;top:27px">
    <span class="brand__dot"></span>
    <span class="brand__name">Linden<br>Foot &amp; Ankle<small>steadystride.com</small></span>
  </div>
  <address class="abs address">58 Orchard Hill Rd<br>Ste. 210, Linden, MD 21000</address>

  <h2 class="abs tagline">
    <div class="tagline__big">We Keep</div>
    <div class="tagline__small">You Moving</div>
  </h2>

  <div class="abs notice">
    <p class="notice__lead">We are pleased to inform<br>that you may be eligible for a<br><em>NEW</em> pair of shoes &amp; inserts!</p>
    <p class="notice__call">Please call our office to<br>schedule your appointment.</p>
    <p class="notice__away">We Are A Phone Call Away</p>
    <p class="notice__phone">(877)555-0142</p>
    <p class="notice__fine">*Last day to place a shoe order is 10/31/23.*<br>**If you have received your shoes and<br>inserts for 2023, please disregard.**</p>
  </div>
</section>

</body>
</html>
```